Executive Coach needs elegant business card design

I need a business card design which includes following info: name, email (same as name, @gmail.com), phone. I'd put that on one side. On the other side i'd like some graphic indicating what i do:
- using questions to help people get great results
- encourage people to try different solutions to overcome old problems
- untangling the mental knot that traps people in vicious circles
- question mental models to get people to see a different point of view.

I'd like an elegant design. Bonus points for providing a different twist on things. I've included 2 designs I started with. Feel free to improve or discard them :-)

```html
<!DOCTYPE html>
<html lang="en">
<head>
<meta charset="UTF-8">
<title>Martin Delorme – Executive Coach Business Card</title>
<link rel="stylesheet" href="https://fonts.googleapis.com/css2?family=Oswald:wght@300;400;500;700&display=swap">
<style>
  :root {
    --page-bg: #ecebe8;
    --card-white: #f3f3f3;
    --card-grey: #cdc9cb;
    --icon-column: #f1f1f1;
    --ink-dark: #2b2b2d;
    --ink-mid: #4f4c4f;
    --ink-soft: #8d898c;
    --orange-1: #e8771f;
    --orange-2: #f29c1d;
    --yellow-1: #f3c420;
    --yellow-2: #f1e73b;
    --blue-1: #2f3f87;
    --blue-2: #4b60a5;
    --blue-3: #7a97ca;
    --blue-4: #a6c7e8;
    --text-light-blue: #aecdf1;
    --text-mid-blue: #4f67aa;
    --text-navy: #27387e;
    --icon-grey: #6c6a6c;
  }
  * { box-sizing: border-box; margin: 0; padding: 0; }
  html, body { width: 1200px; height: 1000px; overflow: hidden; }
  body {
    background: var(--page-bg);
    position: relative;
    font-family: "Oswald", "Arial Narrow", sans-serif;
  }
  .card {
    position: absolute;
    width: 640px;
    height: 370px;
    overflow: hidden;
    box-shadow: 0 4px 14px rgba(0,0,0,.18);
  }

  /* ---------- Front: contact side ---------- */
  .card-front { left: 500px; top: 70px; background: var(--card-white); }
  .accent-stripe {
    position: absolute; left: 0; top: 0; bottom: 0; width: 78px;
    display: flex; flex-direction: column;
  }
  .accent-stripe span { flex: 1; }
  .accent-stripe .s1 { background: var(--orange-1); }
  .accent-stripe .s2 { background: var(--orange-2); }
  .accent-stripe .s3 { background: var(--yellow-1); }
  .accent-stripe .s4 { background: var(--yellow-2); }
  .contact-name {
    position: absolute; right: 30px; top: 34px;
    font-weight: 700; font-size: 44px; letter-spacing: 1px;
    color: var(--ink-dark); text-transform: uppercase;
  }
  .name-rule {
    position: absolute; left: 130px; right: 20px; top: 118px;
    height: 1px; background: #d6d4d5;
  }
  .contact-line {
    position: absolute; right: 30px;
    display: flex; align-items: center; gap: 12px;
    font-weight: 400; font-size: 36px; color: var(--ink-mid);
  }
  .contact-email { top: 128px; }
  .contact-phone { top: 190px; }
  .contact-line svg { flex: none; }
  .tagline-band {
    position: absolute; left: 78px; right: 0; bottom: 0; height: 108px;
    background: var(--card-grey);
  }
  .tagline {
    position: absolute; right: 30px; bottom: 24px;
    font-weight: 400; font-size: 26px; color: var(--ink-soft);
  }

  /* ---------- Back: services side ---------- */
  .card-back { left: 80px; top: 540px; background: var(--icon-column); }
  .service-list {
    position: absolute; left: 0; top: 0; width: 510px; height: 100%;
    display: flex; flex-direction: column;
  }
  .service-row {
    flex: 1; display: flex; align-items: center;
  }
  .service-row .question {
    width: 230px; text-align: right; padding-right: 14px;
    font-weight: 500; font-size: 30px; text-transform: uppercase;
    border-right: 1px solid currentColor; line-height: 54px;
  }
  .service-row .answer {
    padding-left: 14px; font-weight: 400; font-size: 30px; white-space: nowrap;
  }
  .row-1 { background: var(--blue-1); color: var(--text-light-blue); }
  .row-2 { background: var(--blue-2); color: var(--text-light-blue); }
  .row-3 { background: var(--blue-3); color: var(--text-mid-blue); }
  .row-4 { background: var(--blue-4); color: var(--text-navy); }
  .row-1 .question, .row-2 .question { border-color: rgba(174,205,241,.45); }
  .icon-column {
    position: absolute; left: 510px; top: 0; width: 104px; height: 100%;
    display: flex; flex-direction: column;
  }
  .icon-column .icon { flex: 1; display: flex; align-items: center; justify-content: center; }
  .edge-stripe {
    position: absolute; right: 0; top: 0; bottom: 0; width: 26px;
    display: flex; flex-direction: column;
  }
  .edge-stripe span { flex: 1; }
  .edge-stripe .s1 { background: var(--orange-1); }
  .edge-stripe .s2 { background: var(--orange-2); }
  .edge-stripe .s3 { background: var(--yellow-1); }
  .edge-stripe .s4 { background: var(--yellow-2); }
</style>
</head>
<body>

<section class="card card-front" aria-label="Business card front">
  <div class="accent-stripe"><span class="s1"></span><span class="s2"></span><span class="s3"></span><span class="s4"></span></div>
  <h1 class="contact-name">Martin Delorme</h1>
  <div class="name-rule"></div>
  <p class="contact-line contact-email">
    <svg width="44" height="34" viewBox="0 0 44 34" aria-hidden="true">
      <rect x="2" y="8" width="40" height="24" fill="none" stroke="#777" stroke-width="2"/>
      <path d="M2 8 L22 22 L42 8" fill="none" stroke="#777" stroke-width="2"/>
      <circle cx="22" cy="9" r="6" fill="#f3f3f3" stroke="#777" stroke-width="1.6"/>
      <circle cx="22" cy="9" r="2" fill="none" stroke="#777" stroke-width="1.4"/>
    </svg>
    martindelorme@inboxmail.net
  </p>
  <p class="contact-line contact-phone">
    <svg width="24" height="42" viewBox="0 0 24 42" aria-hidden="true">
      <rect x="2" y="2" width="20" height="38" rx="3" fill="none" stroke="#777" stroke-width="2"/>
      <rect x="6" y="7" width="12" height="11" fill="#777"/>
      <g fill="#777"><rect x="6" y="22" width="3" height="3"/><rect x="11" y="22" width="3" height="3"/><rect x="16" y="22" width="3" height="3"/><rect x="6" y="27" width="3" height="3"/><rect x="11" y="27" width="3" height="3"/><rect x="16" y="27" width="3" height="3"/><rect x="6" y="32" width="3" height="3"/><rect x="11" y="32" width="3" height="3"/><rect x="16" y="32" width="3" height="3"/></g>
    </svg>
    614.382507
  </p>
  <div class="tagline-band"></div>
  <p class="tagline">We can help you!!!</p>
</section>

<section class="card card-back" aria-label="Business card back">
  <div class="service-list">
    <div class="service-row row-1"><span class="question">Tired of treat?</span><span class="answer">We can help you!!!</span></div>
    <div class="service-row row-2"><span class="question">Problems from past?</span><span class="answer">Overcome</span></div>
    <div class="service-row row-3"><span class="question">Vicious circles?</span><span class="answer">You can defeat them</span></div>
    <div class="service-row row-4"><span class="question">Mired?</span><span class="answer">Find different solutions</span></div>
  </div>
  <div class="icon-column">
    <div class="icon">
      <svg width="72" height="72" viewBox="0 0 72 72" aria-hidden="true">
        <circle cx="36" cy="36" r="32" fill="none" stroke="var(--icon-grey)" stroke-width="2.5"/>
        <text x="36" y="50" text-anchor="middle" font-family="Oswald, sans-serif" font-size="40" font-weight="300" fill="var(--icon-grey)">?</text>
      </svg>
    </div>
    <div class="icon">
      <svg width="72" height="72" viewBox="0 0 72 72" aria-hidden="true">
        <circle cx="36" cy="36" r="32" fill="none" stroke="var(--icon-grey)" stroke-width="3"/>
        <path d="M22 42 L36 27 L50 42" fill="none" stroke="var(--icon-grey)" stroke-width="3"/>
      </svg>
    </div>
    <div class="icon">
      <svg width="76" height="76" viewBox="0 0 76 76" aria-hidden="true">
        <path d="M12 30 A28 28 0 0 1 62 24" fill="none" stroke="var(--icon-grey)" stroke-width="2"/>
        <path d="M56 22 L63 25 L64 17" fill="none" stroke="var(--icon-grey)" stroke-width="2"/>
        <path d="M64 46 A28 28 0 0 1 14 52" fill="none" stroke="var(--icon-grey)" stroke-width="2"/>
        <path d="M20 54 L13 51 L12 59" fill="none" stroke="var(--icon-grey)" stroke-width="2"/>
      </svg>
    </div>
    <div class="icon">
      <svg width="72" height="72" viewBox="0 0 72 72" aria-hidden="true">
        <circle cx="36" cy="38" r="10" fill="var(--icon-grey)"/>
        <g stroke="var(--icon-grey)" stroke-width="2" fill="none">
          <path d="M36 24 V8 M31 13 L36 8 L41 13"/>
          <path d="M22 38 H6 M11 33 L6 38 L11 43"/>
          <path d="M50 38 H66 M61 33 L66 38 L61 43"/>
        </g>
        <rect x="24" y="54" width="24" height="12" rx="6" fill="var(--icon-grey)"/>
      </svg>
    </div>
  </div>
  <div class="edge-stripe"><span class="s1"></span><span class="s2"></span><span class="s3"></span><span class="s4"></span></div>
</section>

</body>
</html>
```